Postcard For neighbors near worksite

We are a residential interior and exterior painting company. I will be sending post cards out in neighborhoods that we will be currently working in. Basically giving the neighbors a "Neighborhood Notice" that we are in the area and would like to give a Free Estimate to anyone in that neighborhood. I will attach a file of another companies idea that I like. Also, I attached my Logo. Brightfold Painting & More

Target Market(s)

Neighbors near where we are working

Industry/Entity Type

It Company

Requirements
Must have
• Website: Brightfoldpaint.example
• Number: 555.204.6190

```html
<!DOCTYPE html>
<html lang="en">
<head>
<meta charset="utf-8">
<title>Brightfold Painting &amp; More — Neighbors Notice Postcard</title>
<link rel="stylesheet" href="https://fonts.googleapis.com/css2?family=Oswald:wght@300;500;700&family=Open+Sans:wght@400;600&display=swap">
<style>
  :root{
    --page:#ecebe8;
    --panel-dark:#2b2b2c;
    --panel-mid:#4a4a4c;
    --brand-red:#e8161b;
    --white:#ffffff;
    --ink:#222222;
    --rule:#555555;
    --photo-wall:#8e8d72;
    --photo-terracotta:#b0664f;
    --photo-shirt:#f1f1f1;
  }
  *{box-sizing:border-box;margin:0;padding:0}
  html,body{width:1020px;height:1200px;overflow:hidden}
  body{background:var(--page);position:relative;font-family:"Open Sans",Arial,sans-serif}

  .postcard{position:absolute;left:36px;width:948px;height:517px;background:var(--white);overflow:hidden;box-shadow:0 6px 16px rgba(0,0,0,.35)}
  .postcard--front{top:62px}
  .postcard--back{top:622px}

  .site-photo{position:absolute;left:430px;top:0;width:518px;height:517px;
    background:linear-gradient(100deg,var(--photo-wall) 0%,#a0987a 30%,var(--photo-terracotta) 55%,#9c8f70 80%,var(--photo-wall) 100%)}
  .dark-panel{position:absolute;left:0;top:0;width:948px;height:517px}

  .brand-name{position:absolute;left:60px;top:42px;display:flex;align-items:center;gap:10px;
    font-family:"Oswald",Arial,sans-serif;font-weight:500;font-size:24px;color:var(--white);letter-spacing:.3px}
  .brand-name .brand-mark{width:16px;height:16px;background:var(--brand-red)}

  .headline{position:absolute;left:56px;top:128px;font-family:"Oswald",Arial,sans-serif;line-height:1}
  .headline__top{display:block;font-weight:300;font-size:46px;color:var(--white);letter-spacing:1px}
  .headline__main{display:block;font-weight:700;font-size:86px;color:var(--brand-red);margin-top:4px;letter-spacing:1px}

  .body-copy{color:var(--white);font-size:11.4px;line-height:1.45;text-align:justify}
  .body-copy--front{position:absolute;left:58px;top:278px;width:400px}
  .body-copy--back{position:absolute;left:48px;top:210px;width:390px}

  .call-badge{position:absolute;width:290px;height:110px}
  .call-badge svg{position:absolute;inset:0}
  .call-badge__text{position:absolute;left:56px;top:14px;font-family:"Oswald",Arial,sans-serif;color:var(--white);line-height:1.1}
  .call-badge__label{font-weight:500;font-size:24px}
  .call-badge__phone{font-weight:700;font-size:27px;letter-spacing:.5px}
  .call-badge__web{font-family:"Open Sans",Arial,sans-serif;font-weight:600;font-size:13px;display:flex;align-items:center;gap:5px;margin-top:2px}
  .call-badge__web::before{content:"";width:8px;height:8px;border-radius:50%;background:var(--white)}
  .postcard--front .call-badge{left:62px;top:360px}
  .postcard--back .call-badge{left:40px;top:372px}

  .section-tab{position:absolute;left:0;top:144px;width:228px;height:54px;background:var(--brand-red);
    font-family:"Oswald",Arial,sans-serif;font-weight:500;font-size:25px;color:var(--white);padding:10px 0 0 48px}

  .stamp-box{position:absolute;left:780px;top:41px;width:136px;height:130px;border:1px solid var(--rule)}
  .address-line{position:absolute;left:602px;width:313px;border-top:1px solid var(--rule)}
</style>
</head>
<body>

<section class="postcard postcard--front">
  <div class="site-photo" role="img" aria-label="Photo of the painting crew in white shirts working on an exterior wall, with the owner smiling in front"></div>
  <svg class="dark-panel" viewBox="0 0 948 517" aria-hidden="true">
    <defs>
      <radialGradient id="panelFront" cx="35%" cy="40%" r="70%">
        <stop offset="0" stop-color="#56565a"/>
        <stop offset="1" stop-color="#262627"/>
      </radialGradient>
    </defs>
    <polygon fill="url(#panelFront)" points="0,0 470,0 452,18 488,34 446,52 478,70 440,92 484,110 450,128 470,148 432,170 476,190 444,212 462,232 420,256 470,276 438,298 466,318 426,340 458,362 434,384 472,404 440,428 460,450 428,474 456,494 440,517 0,517"/>
  </svg>
  <div class="brand-name"><span class="brand-mark"></span>Brightfold Painting &amp; More</div>
  <h1 class="headline"><span class="headline__top">NEIGHBORS</span><span class="headline__main">NOTICE</span></h1>
  <p class="body-copy body-copy--front">Lorem Ipsum is simply dummy text of the printing and typesetting industry. Lorem Ipsum has been the industry's standard dummy text ever since the 1500s, when an unknown printer took a galley of type and scrambled it to make a type specimen book.</p>
  <div class="call-badge">
    <svg viewBox="0 0 290 110" aria-hidden="true"><polygon fill="var(--brand-red)" points="20,14 60,4 120,10 190,2 250,8 280,20 272,38 290,56 270,72 284,92 240,100 170,108 110,102 50,106 14,96 24,78 2,60 18,44 6,28"/></svg>
    <div class="call-badge__text">
      <div class="call-badge__label">Call Now</div>
      <div class="call-badge__phone">555.204.6190</div>
      <div class="call-badge__web">Brightfoldpaint.example</div>
    </div>
  </div>
</section>

<section class="postcard postcard--back">
  <svg class="dark-panel" viewBox="0 0 948 517" aria-hidden="true">
    <defs>
      <radialGradient id="panelBack" cx="30%" cy="35%" r="75%">
        <stop offset="0" stop-color="#56565a"/>
        <stop offset="1" stop-color="#262627"/>
      </radialGradient>
    </defs>
    <polygon fill="url(#panelBack)" points="0,0 412,0 394,20 428,40 400,62 440,84 410,108 452,130 418,154 462,178 430,202 470,226 436,250 476,276 440,300 482,324 446,348 486,372 452,396 490,420 456,444 482,468 450,492 474,517 0,517"/>
  </svg>
  <div class="brand-name"><span class="brand-mark"></span>Brightfold Painting &amp; More</div>
  <div class="section-tab">Lorem Ipsum</div>
  <p class="body-copy body-copy--back">Lorem Ipsum is simply dummy text of the printing and typesetting industry. Lorem Ipsum has been the industry's standard dummy text ever since the 1500s, when an unknown printer took a galley of type and scrambled it to make a type specimen book. It has survived not only five centuries, but also the leap into electronic typesetting, remaining essentially unchanged. It was popularised in the 1960s with the release of Letraset sheets containing Lorem Ipsum passages, and more recently with desktop publishing software like Aldus PageMaker including versions of Lorem Ipsum.</p>
  <div class="call-badge">
    <svg viewBox="0 0 290 110" aria-hidden="true"><polygon fill="var(--brand-red)" points="20,14 60,4 120,10 190,2 250,8 280,20 272,38 290,56 270,72 284,92 240,100 170,108 110,102 50,106 14,96 24,78 2,60 18,44 6,28"/></svg>
    <div class="call-badge__text">
      <div class="call-badge__label">Call Now</div>
      <div class="call-badge__phone">555.204.6190</div>
      <div class="call-badge__web">Brightfoldpaint.example</div>
    </div>
  </div>
  <div class="stamp-box"></div>
  <div class="address-line" style="top:269px"></div>
  <div class="address-line" style="top:327px"></div>
  <div class="address-line" style="top:384px"></div>
</section>

</body>
</html>
```